Industry / Entity Type

Financial consultancy / advisers

Current site is: http://www.brookvale-partners.com

Looking for a complete overhaul of this site, we are after a clean modern look. Will require the ability to easily add, update and remove content, hence the WordPress design.
Example:
Add case studies
Industry documentation (downloadable brochures / flyers and such)

What we like from our current site is the colour the fonts and the logo (the city of London) we would like to have other city outlines (NYC and Tokyo, Hong Kong, Singapore).

The site will be used by our potential clients to get in contact and re-view the case studies, if possible would like to have a client login area where they can download our documents like NDA’s etc and T&C’s.

Task Outline

Create a Web Design (Coded - Design and coding required)
Designer must provide full implementation/coding depending on the platform chosen by the client (i.e. WordPress theme, HTML/CSS, bootstrap etc.)

Task Description

I need a full website built that must work on desktop and mobile. I can provide the London city skyline and the font file, which we have used. Some stock industrial photos will be required.

Requirements:

*Splash page
*What We Do
*How We do it
*Who Are We? To have the same information and links as the current site
*Why use us?
*Clients: To have the same information and links as the current site
*Partners: To have the same information and links as the current site
*Contact:

Target Market(s)

Financial institutions trading Equities, Futures, Options, Forex and Fixed Income.
Regulators, Exchanges, ECN’s
Buy side firms and Sell side firms

Industry/Entity Type

Financial

Coding

Coded - Design and coding required

Number of Pages Required

5+ page

Font styles to use
Sans Serif

Colors
f04a50

Requirements
Must have
• Splash page
• What We Do
• How We do it
• Who Are We? To have the same information and links as the current site
• Why use us?
• Clients: To have the same information and links as the current site
• Partners: To have the same information and links as the current site
• Contact:

```html
<!DOCTYPE html>
<html lang="en">
<head>
<meta charset="utf-8">
<title>Brookvale Partners</title>
<link href="https://fonts.googleapis.com/css2?family=Michroma&family=Montserrat:wght@400;500&family=Open+Sans:wght@400&display=swap" rel="stylesheet">
<style>
:root{
  --accent:#f04a50;
  --ink:#333333;
  --muted:#666666;
  --white:#ffffff;
  --news-bg:#ececec;
  --footer-bg:#222222;
  --footer-text:#dddddd;
  --social-bg:#2d2d2d;
}
*{margin:0;padding:0;box-sizing:border-box}
html,body{width:844px;height:1200px;overflow:hidden;background:var(--white)}
body{position:relative;font-family:"Open Sans",Arial,sans-serif;color:var(--ink)}
.display{font-family:"Michroma",sans-serif;font-weight:400}
.sans{font-family:"Montserrat",sans-serif}

/* hero */
.hero{position:absolute;left:0;top:0;width:844px;height:395px;overflow:hidden}
.hero-photo{position:absolute;inset:0;background:linear-gradient(180deg,#26385e 0%,#3c4f78 30%,#8a6d6a 52%,#c08a63 62%,#3a3c4a 75%,#6b6470 90%,#8c8590 100%)}
.hero-photo::after{content:"";position:absolute;inset:0;background:rgba(10,15,30,.25)}
.brand{position:absolute;left:292px;top:14px;width:260px;text-align:center}
.brand-skyline{width:242px;height:56px;margin:0 auto;background:linear-gradient(180deg,rgba(255,255,255,0) 0%,rgba(255,255,255,.28) 100%);border-bottom:1px solid rgba(255,255,255,.7)}
.brand-name{margin-top:8px;color:var(--white);font-size:11px;letter-spacing:2px;line-height:14px}
.main-nav{position:absolute;top:139px;left:0;width:844px;display:flex;justify-content:center;gap:25px}
.main-nav a{color:var(--white);font-family:"Montserrat",sans-serif;font-size:8.5px;text-decoration:none;letter-spacing:.2px}
.hero-title{position:absolute;top:203px;left:0;width:844px;text-align:center;color:var(--white);font-size:28px;letter-spacing:2px}
.hero-sub{position:absolute;top:256px;left:0;width:844px;text-align:center;color:var(--white);font-family:"Montserrat",sans-serif;font-size:13px;letter-spacing:.5px}
.btn{display:inline-block;background:var(--accent);color:var(--white);font-family:"Montserrat",sans-serif;text-decoration:none;border-radius:2px}
.hero-btn{position:absolute;left:367px;top:296px;width:110px;height:31px;line-height:31px;text-align:center;font-size:11px}
.slider-arrow{position:absolute;top:218px}
.slider-arrow.prev{left:71px}.slider-arrow.next{left:753px}

/* what we do */
.services{position:absolute;top:395px;left:0;width:844px;height:284px}
.section-title{position:absolute;left:0;width:844px;text-align:center;font-size:24px;letter-spacing:3px;color:var(--ink)}
.services .section-title{top:32px}
.service{position:absolute;top:92px;width:200px;text-align:center}
.service svg{display:block;margin:0 auto}
.service h3{margin-top:14px;color:var(--accent);font-family:"Montserrat",sans-serif;font-weight:400;font-size:14px;letter-spacing:.3px}
.service p{margin-top:12px;color:var(--muted);font-size:8px;line-height:17px}

/* news */
.news{position:absolute;top:679px;left:0;width:844px;height:301px;background:var(--news-bg)}
.news .section-title{top:40px}
.news-card{position:absolute;top:114px;width:330px;height:134px}
.news-photo{position:absolute;left:0;top:0;width:150px;height:133px}
.news-body{position:absolute;left:166px;top:0;width:160px}
.news-body h3{color:var(--accent);font-family:"Montserrat",sans-serif;font-weight:400;font-size:11px;line-height:14px;letter-spacing:.2px}
.news-body p{margin-top:9px;color:var(--muted);font-size:8px;line-height:17px}
.news-body .btn{position:absolute;top:113px;left:1px;width:68px;height:20px;line-height:20px;text-align:center;font-size:8px}

/* footer */
.site-footer{position:absolute;top:980px;left:0;width:844px;height:220px;background:var(--footer-bg);color:var(--footer-text)}
.footer-brand{position:absolute;left:93px;top:30px;width:230px}
.footer-brand .brand-skyline{width:229px;height:52px;margin:0}
.footer-brand .brand-name{text-align:center;font-size:10px;letter-spacing:1.8px}
.footer-about{position:absolute;left:93px;top:127px;width:240px;font-size:8px;line-height:17px}
.copyright{position:absolute;left:93px;top:179px;font-size:8px;color:var(--white)}
.footer-col{position:absolute;top:29px}
.footer-col h4{font-family:"Montserrat",sans-serif;font-weight:400;font-size:11px;color:var(--white);letter-spacing:.3px}
.quick-links{left:369px}
.quick-links ul{list-style:none;margin-top:14px}
.quick-links li{font-size:8px;line-height:17.5px}
.contact{left:493px;width:140px}
.contact ul{list-style:none;margin-top:14px}
.contact li{position:relative;padding-left:17px;font-size:8px;line-height:11px;margin-bottom:8px;color:var(--white)}
.contact li svg{position:absolute;left:0;top:1px}
.contact a{color:var(--white)}
.social{position:absolute;left:630px;top:32px;display:flex;gap:2px}
.social span{display:block;width:40px;height:30px;background:var(--social-bg)}
.corner-mark{display:none}
</style>
</head>
<body>

<header class="hero">
  <div class="hero-photo" role="img" aria-label="City skyline at dusk with a suspension bridge over the river"></div>
  <div class="brand">
    <div class="brand-skyline" role="img" aria-label="Line drawing of a city skyline"></div>
    <div class="brand-name display">BROOKVALE PARTNERS</div>
  </div>
  <nav class="main-nav">
    <a href="#">HOME</a><a href="#">WHAT WE DO</a><a href="#">HOW WE DO IT</a><a href="#">WHO ARE WE</a><a href="#">WHY USE US</a><a href="#">CLIENTS</a><a href="#">PARTNERS</a><a href="#">CONTACT</a>
  </nav>
  <svg class="slider-arrow prev" width="20" height="20" viewBox="0 0 20 20" aria-label="Previous slide"><circle cx="10" cy="10" r="9.3" fill="none" stroke="#fff" stroke-width="1"/><path d="M11.5 6 L7.5 10 L11.5 14" fill="none" stroke="#fff" stroke-width="1"/></svg>
  <svg class="slider-arrow next" width="20" height="20" viewBox="0 0 20 20" aria-label="Next slide"><circle cx="10" cy="10" r="9.3" fill="none" stroke="#fff" stroke-width="1"/><path d="M8.5 6 L12.5 10 L8.5 14" fill="none" stroke="#fff" stroke-width="1"/></svg>
  <h1 class="hero-title display">Genuine Motivation</h1>
  <p class="hero-sub">TO SEE OUR CLIENTS SUCCEED</p>
  <a class="btn hero-btn" href="#">VIEW DETAILS</a>
</header>

<section class="services">
  <h2 class="section-title display">What we do</h2>
  <article class="service" style="left:89px">
    <svg width="34" height="32" viewBox="0 0 34 32"><ellipse cx="17" cy="17" rx="13" ry="10" fill="none" stroke="#333" stroke-width="1.2"/><circle cx="17" cy="17" r="4" fill="none" stroke="#333" stroke-width="1.2"/><path d="M11 26 v4 M23 26 v4" stroke="#333" stroke-width="1.2"/></svg>
    <h3>MANAGEMENT</h3>
    <p>Today's technology allows our clients to take their knowledge to the market in ways that previous generations could only dream of.</p>
  </article>
  <article class="service" style="left:322px">
    <svg width="34" height="32" viewBox="0 0 34 32"><circle cx="17" cy="14" r="10" fill="none" stroke="#333" stroke-width="1.2"/><path d="M9 5 A13 13 0 0 0 25 25 M17 27 v3 M12 30 h10" fill="none" stroke="#333" stroke-width="1.2"/></svg>
    <h3>RESEARCH</h3>
    <p>Today's technology allows our clients to take their knowledge to the market in ways that previous generations could only dream of.</p>
  </article>
  <article class="service" style="left:555px">
    <svg width="34" height="32" viewBox="0 0 34 32"><rect x="3" y="3" width="28" height="20" fill="none" stroke="#333" stroke-width="1.2"/><path d="M8 17 L11 9 L14 15 L17 9 M21 13 a2.5 2.5 0 1 0 0.1 0 M17 23 v3 M11 30 L17 26 L23 30" fill="none" stroke="#333" stroke-width="1.2"/></svg>
    <h3>TRAINNING</h3>
    <p>Today's technology allows our clients to take their knowledge to the market in ways that previous generations could only dream of.</p>
  </article>
</section>

<section class="news">
  <h2 class="section-title display">Recent News</h2>
  <article class="news-card" style="left:93px">
    <div class="news-photo" role="img" aria-label="Hands working at a keyboard and mouse on a white desk" style="background:linear-gradient(135deg,#d9dcdf 0%,#b9bdc2 50%,#4b4f55 100%)"></div>
    <div class="news-body">
      <h3>BROOKVALE PARTNERS IN 2014</h3>
      <p>Today's technology allows our clients to take their knowledge to the market in ways that previous generations could only dream of.</p>
      <a class="btn" href="#">READ MORE</a>
    </div>
  </article>
  <article class="news-card" style="left:442px">
    <div class="news-photo" role="img" aria-label="Business people shaking hands in a bright office lobby" style="background:linear-gradient(135deg,#e3b08a 0%,#a8745a 45%,#3c2f30 100%)"></div>
    <div class="news-body">
      <h3>BROOKVALE PARTNERS IN 2014</h3>
      <p>Today's technology allows our clients to take their knowledge to the market in ways that previous generations could only dream of.</p>
      <a class="btn" href="#">READ MORE</a>
    </div>
  </article>
</section>

<footer class="site-footer">
  <div class="footer-brand">
    <div class="brand-skyline" role="img" aria-label="Line drawing of a city skyline"></div>
    <div class="brand-name display">BROOKVALE PARTNERS</div>
  </div>
  <p class="footer-about">Since founding Brookvale Partners in 2014 we have dedicated ourselves to the provision of services.</p>
  <p class="copyright">© 2017 Brookvale-partners.com. All Right Reserved</p>
  <div class="footer-col quick-links">
    <h4>QUICK LINKS</h4>
    <ul><li>Home</li><li>What we do</li><li>How we do it</li><li>Who are we</li><li>Why use us</li><li>Clients</li><li>Partners</li><li>Contact</li></ul>
  </div>
  <div class="footer-col contact">
    <h4>CONTACT US</h4>
    <ul>
      <li><svg width="9" height="9" viewBox="0 0 9 9"><path d="M1 3 Q4.5 0 8 3 L7 4 L6 3 H3 L2 4 Z M2 5 H7 V8 H2 Z" fill="#ddd"/></svg>1-555-014-2226</li>
      <li><svg width="9" height="9" viewBox="0 0 9 9"><rect x="2" y="0.5" width="5" height="3" fill="none" stroke="#ddd"/><rect x="0.5" y="3.5" width="8" height="3.5" fill="#ddd"/><rect x="2" y="6" width="5" height="2.5" fill="none" stroke="#ddd"/></svg>1-555-014-2227</li>
      <li><svg width="9" height="9" viewBox="0 0 9 9"><rect x="0.5" y="1.5" width="8" height="6" fill="none" stroke="#ddd"/><path d="M0.5 1.5 L4.5 5 L8.5 1.5" fill="none" stroke="#ddd"/></svg><a href="#">info@brookvale-partners.com</a></li>
      <li><svg width="9" height="10" viewBox="0 0 9 10"><path d="M4.5 10 L1.3 5 A3.5 3.5 0 1 1 7.7 5 Z" fill="#ddd"/><circle cx="4.5" cy="3.5" r="1.3" fill="#222"/></svg>#2868 Lorem ipsum dolor sit amet, consectetur</li>
    </ul>
  </div>
  <div class="social" aria-label="Social links"><span></span><span></span><span></span></div>
</footer>

</body>
</html>
```